design a construction company business card

Design business card around our logo. Card must have all the typical info: name, title, address, phone, email, business name, etc. Somewhere on the card I would like to see our motto "Built with care... Driven by craft." Consider adding a splash of bright orange to the card to complement the blues and silvers/grays in the logo. We are open to metallic inks, textures, etc. We would like to see options on both light and dark backgrounds. The font in the logo is Euro Technic Extended Regular.

```html
<!DOCTYPE html>
<html lang="en">
<head>
<meta charset="utf-8">
<title>Halvorsen Contracting – Business Card</title>
<link rel="stylesheet" href="https://fonts.googleapis.com/css2?family=Michroma&family=Montserrat:wght@400;700&display=swap">
<style>
  :root {
    --stage: #15171a;
    --card: #24282c;
    --card-edge: #2c3136;
    --silver: #c9ccd0;
    --white: #f2f3f5;
    --blue: #2f62d6;
    --blue-soft: #3d6fe0;
  }
  * { box-sizing: border-box; margin: 0; padding: 0; }
  html, body {
    width: 1200px; height: 800px; overflow: hidden;
    background: var(--stage);
  }
  .canvas {
    width: 1200px; height: 800px;
    display: flex; flex-direction: column; align-items: center; justify-content: center;
    gap: 40px;
  }
  .card {
    width: 560px; height: 320px;
    background: var(--card);
    border: 1px solid var(--card-edge);
    border-radius: 16px;
    position: relative;
    overflow: hidden;
  }

  /* Brand name: plain text, one colour, one weight */
  .brand {
    font-family: "Montserrat", sans-serif;
    font-weight: 700;
    font-size: 24px;
    letter-spacing: 0.5px;
    line-height: 1;
    white-space: nowrap;
  }

  /* Front */
  .card--front {
    display: flex; flex-direction: column; align-items: center; justify-content: center;
  }
  .card--front .brand { color: var(--silver); }
  .motto {
    font-family: "Montserrat", sans-serif; font-weight: 700;
    font-size: 14px; color: var(--white);
    margin-top: 24px;
    letter-spacing: 0.3px;
  }

  /* Back */
  .card--back .brand {
    position: absolute; left: 40px; top: 56px;
    color: var(--blue);
  }

  .person {
    position: absolute; left: 40px; top: 160px;
    font-family: "Michroma", sans-serif;
  }
  .person__name { color: var(--blue-soft); font-size: 15px; letter-spacing: 1px; }
  .person__title { color: var(--white); font-size: 11px; margin-top: 6px; }

  .rule {
    position: absolute; left: 40px; right: 24px; top: 216px;
    height: 1px; background: var(--blue);
  }

  .contacts {
    position: absolute; left: 40px; top: 230px;
    list-style: none;
    font-family: "Michroma", sans-serif; font-size: 10.5px; color: var(--white);
  }
  .contacts li { display: flex; align-items: center; gap: 10px; height: 21px; }
  .contacts svg { width: 12px; height: 12px; flex: none; }
  .contacts .accent { color: var(--blue-soft); }

  .address {
    position: absolute; right: 28px; top: 150px;
    text-align: right;
    font-family: "Michroma", sans-serif; font-size: 10.5px; line-height: 1.6;
    color: var(--white); font-style: normal;
  }
</style>
</head>
<body>
<main class="canvas">

  <section class="card card--front" aria-label="Card front">
    <div class="brand">HALVORSEN CONTRACTING, INC.</div>
    <p class="motto">Built with care... Driven by craft.</p>
  </section>

  <section class="card card--back" aria-label="Card back">
    <div class="brand">HALVORSEN CONTRACTING, INC.</div>

    <address class="address">
      4821 Quarry Road<br>
      Suite 7, Dunmore<br>
      MD 21904
    </address>

    <div class="person">
      <div class="person__name">DANA KERR</div>
      <div class="person__title">CEO</div>
    </div>

    <div class="rule"></div>

    <ul class="contacts">
      <li>
        <svg viewBox="0 0 12 12" aria-hidden="true"><rect x="3" y="1" width="6" height="10" rx="1" fill="none" stroke="#3d6fe0" stroke-width="1.2"/></svg>
        <span>410 555 0187</span>
      </li>
      <li>
        <svg viewBox="0 0 12 12" aria-hidden="true"><rect x="1" y="2.5" width="10" height="7" fill="#3d6fe0"/><path d="M1 2.5 L6 6.5 L11 2.5" fill="none" stroke="#24282c" stroke-width="1"/></svg>
        <span>info@halvorsenbuild.com</span>
      </li>
      <li>
        <svg viewBox="0 0 12 12" aria-hidden="true"><circle cx="6" cy="6" r="5" fill="#3d6fe0"/><path d="M1 6 H11 M6 1 C3.5 4 3.5 8 6 11 M6 1 C8.5 4 8.5 8 6 11" fill="none" stroke="#24282c" stroke-width="0.8"/></svg>
        <span>www.<span class="accent">halvorsenbuild</span>.com</span>
      </li>
    </ul>
  </section>

</main>
</body>
</html>
```